Artistic Poster for a Short Film

I am the Writer/Director of an upcoming short film called "Driftwater" and I need a 20x30 poster for the project screening. The screening is coming up very soon so apologies for the quick turnaround time. Here is a short synopsis:

"Walter is a mysterious man who is lost and disoriented. With the help of Marisol, he searches for items out of an old diary written long ago by a woman named Gloria, despite not understanding exactly why he does so. Marisol helps, but when they are unsuccessful she confronts Walter: Does he know why he restlessly searches for these items? The truth is shocking, and reveals Walter's connections to Marisol, Gloria, and the strange old diary.

The truth is that Walter is actually an old man, and Marisol is his caretaker and granddaughter. His memories, including those of Gloria, his deceased wife, have been destroyed by Dementia. He often wakes believing himself to be at an earlier stage of his life, and therefore meets many of the challenges of life with anger and confusion."

Here is the film's website: http://www.driftwater-film.example
Here is our successful Fundbarrow: http://www.fundbarrow.example/projects/502847719/driftwater-a-short-film

The design should be dark and simple. I'm a fan of the art-prints that this short film used (scroll down to see): http://www.fundbarrow.example/projects/ruthvanderlo/kettle-a-short-film-based-on-the-story-by-omar-quill but I'm also open to other ideas. If you google "alternative movie posters" you'll see what I mean. The poster should be simple, easy to read, and hint at the themes of the film without giving the twist away.

Here is a link to the Fine Cut of the film: https://clipvault.example/48210576 The password is: lanterns72
It is not a completed version but will give you an idea of what the film will look like.

Target Market(s)

The intended audience is an art-film crowd of moviegoers.

Industry/Entity Type

Movie

Requirements
Must have
• The poster must have the typical movie poster text at the bottom. The information that should be included is: First line: COPPER LANTERN STUDIOS presents a film by DANIEL OSTROM "DRIFTWATER" MARCEL BRUNAUD TERRA WOLCOTT
Second line: music by OWEN PRATT director of photography VICTOR L. MORALES edited by SIMON ORR costume designer ROBERTA CLINE
Third line: produced by GAIL TORVALD DANIEL OSTROM written and directed by DANIEL OSTROM

It should have the title of the film "Driftwater" and "A film by Daniel Ostrom" on the poster (in addition to the text at the bottom.

It must be high-quality and printable to a size of 20x30. Ideal resolution is 6060x9090. I only need the high quality printable file, I will do the printing myself.
Should not have
• Bright colors.

```html
<!DOCTYPE html>
<html lang="en">
<head>
<meta charset="utf-8">
<title>Driftwater — Poster</title>
<link rel="stylesheet" href="https://fonts.googleapis.com/css2?family=Cinzel:wght@400;500&family=Marcellus&family=Oswald:wght@400;500;600&display=swap">
<style>
  :root {
    --ink-black: #050605;
    --forest-deep: #0d140f;
    --forest-mid: #1f2a22;
    --mist: #b9bcbb;
    --road: #2a2c2c;
    --title-red: #e01010;
    --text-white: #f2f2f2;
    --rule-grey: #9a9a9a;
  }
  * { margin: 0; padding: 0; box-sizing: border-box; }
  html, body {
    width: 800px; height: 1200px; overflow: hidden;
    background: var(--ink-black);
  }
  .poster {
    position: relative;
    width: 800px; height: 1200px;
    overflow: hidden;
    color: var(--text-white);
    font-family: "Oswald", "Arial Narrow", sans-serif;
    text-align: center;
  }
  .poster-photo {
    position: absolute; inset: 0;
    background:
      radial-gradient(ellipse 60px 330px at 50% 18%, rgba(190,194,193,0.85), rgba(120,126,124,0.35) 55%, transparent 100%),
      radial-gradient(ellipse 140px 260px at 50% 90%, rgba(60,62,62,0.55), transparent 100%),
      linear-gradient(90deg, var(--ink-black) 0%, var(--forest-deep) 18%, var(--forest-mid) 38%, #3a4540 50%, var(--forest-mid) 62%, var(--forest-deep) 82%, var(--ink-black) 100%);
  }
  .poster-photo::after {
    content: ""; position: absolute; inset: 0;
    background: linear-gradient(180deg, rgba(0,0,0,0.35) 0%, rgba(0,0,0,0.1) 25%, rgba(0,0,0,0.55) 50%, rgba(0,0,0,0.75) 80%, rgba(0,0,0,0.85) 100%);
  }
  .layer { position: absolute; left: 0; width: 100%; }
  .title-main {
    top: 490px;
    font-family: "Cinzel", "Times New Roman", serif;
    font-weight: 400;
    font-size: 66px;
    letter-spacing: 3px;
    color: var(--title-red);
  }
  .title-byline {
    top: 578px;
    font-family: "Marcellus", "Times New Roman", serif;
    font-size: 27px;
    letter-spacing: 1px;
    color: var(--title-red);
  }
  .starring {
    top: 816px; left: 240px; width: 311px;
    height: 21px;
    border-top: 1px solid var(--rule-grey);
    border-bottom: 1px solid var(--rule-grey);
    font-size: 10px; font-weight: 500;
    line-height: 19px;
    letter-spacing: 0.5px;
  }
  .cast-name { position: absolute; top: 857px; width: 200px; line-height: 1; }
  .cast-name--left { left: 177px; }
  .cast-name--right { left: 407px; }
  .cast-first { display: block; font-size: 14px; font-weight: 500; }
  .cast-last { display: block; font-size: 31px; font-weight: 500; margin-top: 2px; }
  .presents {
    top: 928px;
    font-size: 10.5px; font-weight: 500; letter-spacing: 0.3px;
  }
  .title-billing {
    top: 945px;
    font-family: "Cinzel", "Times New Roman", serif;
    font-size: 46px;
    letter-spacing: 2px;
    color: var(--title-red);
  }
  .credits {
    font-size: 9.8px; font-weight: 500; letter-spacing: 0.3px;
  }
  .credits--one { top: 1033px; }
  .credits--two { top: 1056px; }
  .release-date {
    top: 1118px;
    font-size: 34px; font-weight: 500; letter-spacing: 1px;
  }
</style>
</head>
<body>
  <main class="poster">
    <div class="poster-photo" role="img" aria-label="Dark photograph of a misty road running straight through a tall evergreen forest, pale sky between the treetops"></div>

    <h1 class="layer title-main">DRIFTWATER</h1>
    <p class="layer title-byline">A film by Daniel Ostrom</p>

    <p class="layer starring">STARRING:</p>
    <p class="cast-name cast-name--left"><span class="cast-first">MARCEL</span><span class="cast-last">BRUNAUD</span></p>
    <p class="cast-name cast-name--right"><span class="cast-first">TERRA</span><span class="cast-last">WOLCOTT</span></p>

    <p class="layer presents">COPPER LANTERN STUDIOS PRESENTS A FILM BY DANIEL OSTROM</p>
    <p class="layer title-billing">DRIFTWATER</p>

    <p class="layer credits credits--one">MUSIC BY OWEN PRATT DIRECTOR OF PHOTOGRAPHY VICTOR L. MORALES EDITED BY SIMON ORR COSTUME DESIGNER ROBERTA CLINE</p>
    <p class="layer credits credits--two">PRODUCED BY GAIL TORVALD DANIEL OSTROM WRITTEN AND DIRECTED BY DANIEL OSTROM</p>

    <p class="layer release-date">01.01.2013</p>
  </main>
</body>
</html>
```